Web site for small printshop

I am looking for a website for small printshop in Iceland, mainly serving university students and artist.

We print posters, flyers, business cards and more.

In addition to our current website, I would like to include design tool, (fx. www.quarvelink.com, www.tandorizo.com or something similar) jobs upload, shopping chart.
Updates

Great work, I am really amazed of the quality of work i am seeing here.

Really way beyond my expectation

GOOD JOB - all of you ! 

Hi all.

The designs submitted have been great, way better than expected.
I really did not expect this level of quality.

Some have been asking me for feedback on their designs, and I will try 
to send some feedback here, without spoiling your creativity.

Likes:
- when the colors of my logo is used in menus, buttons etc.
- simple, not to crowded look.

Dislikes.
- Dark and heavy design
- Lot of text and buttons (crowded look)

Extra info.
- top line (before menus) will contain: Tel - email - language
- menu line will have 5 categories: Home - service - submission of works - FAQ - about us
- 3 large buttons:  Job submit - Job design - ask for offer

LOVE YOUR WORK - great designs so far :)

Target Market(s)

University Students, Artists. Age group 20-30

Industry/Entity Type

University

Requirements
Must have
• The website must be easy to use, clean looking.

```html
<!DOCTYPE html>
<html lang="en">
<head>
<meta charset="utf-8">
<title>Prentvik – Printshop</title>
<link href="https://fonts.googleapis.com/css2?family=Open+Sans:wght@400;600;700;800&display=swap" rel="stylesheet">
<style>
:root{
  --red:#e8322b;
  --yellow:#fed400;
  --ink:#2a2a2a;
  --text:#6f6f6f;
  --muted:#9a9a9a;
  --rule:#e4e4e4;
  --black:#0d0d0d;
  --footer:#161616;
  --white:#fff;
}
*{box-sizing:border-box;margin:0;padding:0}
html,body{width:1200px;height:3236px;overflow:hidden}
body{position:relative;background:var(--white);font-family:"Open Sans",Arial,sans-serif;color:var(--text)}
.section{position:absolute;left:0;width:1200px}
.wrap{position:relative;width:860px;margin:0 auto}
a{color:inherit;text-decoration:none}

/* top bar */
.topbar{top:0;height:65px;background:var(--black);color:var(--white);font-size:13px;font-weight:600}
.topbar .wrap{width:1000px;height:65px;display:flex;align-items:center;justify-content:space-between}
.topbar .contact,.topbar .account{display:flex;align-items:center;gap:28px}
.topbar .item{display:flex;align-items:center;gap:9px}
.dot-icon{width:17px;height:17px;border-radius:50%;background:var(--white);display:inline-flex;align-items:center;justify-content:center}
.account{gap:24px}

/* header */
.header{top:65px;height:132px}
.header .wrap{width:950px;height:132px;display:flex;align-items:center;justify-content:space-between}
.logo{display:flex;align-items:center;gap:12px;font-size:30px;font-weight:800;color:var(--ink);letter-spacing:.5px}
.logo-square{width:34px;height:34px;background:var(--red)}
.nav{display:flex;gap:30px;font-size:15px;font-weight:600;color:var(--ink)}
.nav .active{color:var(--red)}

/* hero */
.hero{top:197px;height:477px;background:linear-gradient(180deg,#9ea3a6 0%,#7f8488 55%,#5a4a3e 100%)}
.hero-strip{position:absolute;left:150px;bottom:0;width:900px;height:12px;display:flex}
.hero-strip span{flex:1}
.hero-strip .y{background:var(--yellow)}.hero-strip .r{background:var(--red)}

/* services */
.services{top:740px;height:240px}
.services .wrap{width:760px;display:flex;justify-content:space-between}
.service{width:230px;text-align:center}
.service-icon{width:90px;height:90px;border-radius:50%;background:var(--red);margin:0 auto 36px;display:flex;align-items:center;justify-content:center}
.service h3{font-size:17px;font-weight:800;color:var(--ink);margin-bottom:12px}
.service p{font-size:11px;line-height:15px;color:var(--muted)}

/* section heading */
.heading{display:flex;align-items:center;gap:22px;font-size:16px;font-weight:800;color:var(--ink);text-transform:uppercase}
.heading::after{content:"";flex:1;height:8px;background:var(--rule)}
.heading.short::after{margin-right:10px}

.more{display:inline-flex;align-items:center;gap:16px;font-size:13px;color:var(--ink)}
.arrow{width:22px;height:22px;background:var(--red);display:inline-flex;align-items:center;justify-content:center}

/* about */
.about{top:1022px}
.about-body{position:absolute;top:68px;left:26px;display:flex;gap:60px}
.about-photo{width:330px;height:184px;background:linear-gradient(135deg,#e6e6e6,#a7a9aa 60%,#5d6266)}
.about-text{width:330px;padding-top:4px}
.about-text h2{font-size:19px;font-weight:400;color:var(--red);line-height:24px;margin-bottom:18px}
.about-text p{font-size:12.5px;line-height:18px;margin-bottom:16px}

/* why */
.why{top:1328px}
.feature-grid{position:absolute;top:60px;left:0;width:860px;display:grid;grid-template-columns:repeat(3,1fr);column-gap:22px}
.feature{height:232px}
.feature h3{font-size:21px;font-weight:400;color:var(--red);margin-bottom:12px}
.feature p{font-size:12.5px;line-height:17px;height:92px;margin-bottom:16px}
.feature .more{gap:30px}
.divider{grid-column:1/-1;border-top:2px dashed var(--rule);height:0;margin:-16px 0 36px}

/* gallery */
.gallery{top:1860px}
.tabs{position:absolute;top:44px;left:12px;width:848px;display:flex;align-items:center;font-size:12.5px;color:var(--ink)}
.tabs span.sep{color:#bbb;margin:0 12px}
.tabs .on{color:var(--red)}
.tab-arrows{margin-left:auto;display:flex;gap:8px}
.tab-arrows .arrow{width:26px;height:26px}
.tiles{position:absolute;top:101px;left:16px;display:grid;grid-template-columns:repeat(3,268px);grid-auto-rows:146px;gap:16px 12px}
.tile-a{background:linear-gradient(135deg,#8aa39a,#5c4a3a)}
.tile-b{background:linear-gradient(135deg,#1f2a3a,#b0463c)}
.tile-c{background:linear-gradient(135deg,#7a5a6a,#c7a06a)}
.tile-d{background:var(--red);color:var(--white);text-align:center;padding-top:28px}
.tile-d h3{font-size:25px;font-weight:800;margin-bottom:12px}
.tile-d p{font-size:12px;line-height:16px}
.tile-e{background:linear-gradient(180deg,#2d3a5a,#c8b9a0)}
.tile-f{background:linear-gradient(135deg,#d9d0b0,#6a5a40)}

/* comments */
.comments{top:2330px}
.comment-grid{position:absolute;top:56px;left:10px;display:flex;gap:40px}
.comment{width:256px}
.quote{font-size:44px;font-weight:700;color:var(--red);line-height:34px;height:30px}
.comment p{font-size:12.5px;line-height:17px;margin-bottom:18px}
.author{display:flex;align-items:center;justify-content:space-between;width:210px;font-size:12px}
.author b{font-weight:400;color:var(--red)}
.avatar{width:60px;height:60px;background:linear-gradient(135deg,#d8d8d8,#8d9194)}

/* partners */
.partners{top:2615px}
.partner-row{position:absolute;top:80px;left:10px;width:850px;display:flex;justify-content:space-between;align-items:center}
.badge{background:#c9c9c9}

/* tweet band */
.tweet{top:2837px;height:116px;background:var(--yellow)}
.tweet .wrap{width:1010px;height:116px;display:flex;align-items:center;gap:30px;font-size:14px;color:var(--ink)}
.tweet-dot{width:30px;height:30px;border-radius:50%;background:var(--red);flex:none}

/* footer */
.footer{top:2953px;height:283px;background:linear-gradient(135deg,#1c1c1c,#0a0a0a);color:#a8a8a8}
.footer-cols{position:absolute;top:34px;left:178px;display:flex;gap:0}
.footer-col h4{font-size:16px;font-weight:400;color:var(--white);margin-bottom:26px}
.footer-col p{font-size:11.5px;line-height:16px;margin-bottom:20px}
.col-about{width:316px;padding-right:60px}
.col-address{width:269px}
.col-extra{width:260px}
.address-list{list-style:none;font-size:11.5px}
.address-list li{display:flex;align-items:center;gap:14px;margin-bottom:14px}
.footer .more{color:var(--white);font-size:12px}
.footer .arrow{width:18px;height:18px}
.footer-bottom{position:absolute;left:0;bottom:0;width:1200px;height:72px;border-top:1px solid #2c2c2c}
.footer-bottom .wrap{width:1010px;height:72px;display:flex;align-items:center;font-size:11.5px;color:#bdbdbd}
.legal-links{margin-left:auto;display:flex;gap:10px;margin-right:70px}
.socials{display:flex;gap:10px}
.socials span{width:22px;height:22px;border-radius:50%;background:#5a5a5a}
</style>
</head>
<body>

<header class="section topbar">
  <div class="wrap">
    <div class="contact">
      <span class="item"><span class="dot-icon"><svg width="10" height="10" viewBox="0 0 10 10"><path d="M2 1l2 2-1 1.2c.6 1.2 1.6 2.2 2.8 2.8L7 6l2 2-1.3 1.3C4.5 9 1 5.5.7 2.3z" fill="#0d0d0d"/></svg></span>+354 512 4080</span>
      <span class="item"><span class="dot-icon"><svg width="10" height="8" viewBox="0 0 10 8"><rect x=".5" y=".5" width="9" height="7" fill="none" stroke="#0d0d0d"/><path d="M.5.5L5 4.5 9.5.5" fill="none" stroke="#0d0d0d"/></svg></span>info@prentvik.is</span>
    </div>
    <div class="account">
      <span>WELCOME MSG!</span><span>My Account</span><span>My Cart</span><span>Checkout</span>
      <span class="item"><svg width="18" height="16" viewBox="0 0 18 16"><path d="M1 1h3l2 9h9l2-7H5" fill="none" stroke="#e8322b" stroke-width="2"/><circle cx="7" cy="14" r="1.5" fill="#e8322b"/><circle cx="14" cy="14" r="1.5" fill="#e8322b"/></svg>$ 0.00</span>
      <span>language ▾</span><span>USD ▾</span>
      <svg width="15" height="15" viewBox="0 0 15 15"><circle cx="6" cy="6" r="4.5" fill="none" stroke="#fff" stroke-width="2"/><path d="M9.5 9.5L14 14" stroke="#fff" stroke-width="2"/></svg>
    </div>
  </div>
</header>

<div class="section header">
  <div class="wrap">
    <a class="logo" href="#"><span class="logo-square"></span>PRENTVIK</a>
    <nav class="nav">
      <a class="active" href="#">Home</a><a href="#">Service</a><a href="#">Submission of Works</a><a href="#">FAQs</a><a href="#">Contact us</a>
    </nav>
  </div>
</div>

<section class="section hero" role="img" aria-label="Smiling student leaning on a stack of books in front of a chalkboard with formulas">
  <div class="hero-strip"><span class="y"></span><span class="r"></span><span class="y"></span></div>
</section>

<section class="section services">
  <div class="wrap">
    <div class="service">
      <div class="service-icon"><svg width="40" height="40" viewBox="0 0 40 40"><rect x="8" y="6" width="24" height="28" rx="3" fill="#fff" transform="rotate(-12 20 20)"/><path d="M13 14h14M13 20h14M13 26h9" stroke="#e8322b" stroke-width="3" transform="rotate(-12 20 20)"/></svg></div>
      <h3>JOB SUBMIT</h3>
      <p>perspiciatis unde omnis iste natus error sit voluptatem accusantium dolore laudantium</p>
    </div>
    <div class="service">
      <div class="service-icon"><svg width="40" height="40" viewBox="0 0 40 40"><path d="M10 30l3-9 15-15 6 6-15 15z" fill="#fff"/><path d="M10 30l3-9 6 6z" fill="#f6b7b3"/></svg></div>
      <h3>JOB DESIGN</h3>
      <p>perspiciatis unde omnis iste natus error sit voluptatem accusantium dolore laudantium</p>
    </div>
    <div class="service">
      <div class="service-icon"><svg width="42" height="40" viewBox="0 0 42 40"><ellipse cx="21" cy="18" rx="16" ry="12" fill="#fff"/><path d="M12 27l-2 8 9-6z" fill="#fff"/><ellipse cx="21" cy="18" rx="9" ry="5" fill="#e8322b"/></svg></div>
      <h3>ASK FOR OFFER</h3>
      <p>perspiciatis unde omnis iste natus error sit voluptatem accusantium dolore laudantium</p>
    </div>
  </div>
</section>

<section class="section about">
  <div class="wrap">
    <h2 class="heading">Who we are</h2>
    <div class="about-body">
      <div class="about-photo" role="img" aria-label="Portrait of a young man in a shirt"></div>
      <div class="about-text">
        <h2>Sed enim accusantium<br>laudantium laudantium sunt</h2>
        <p>Sed enim accusantium laudantium Unde quasi quae ratione iste sunt sed sit ipsam voluptatem consequuntur iste ipsam ratione ratione dolores consequuntur ut consequuntur architecto sunt perspiciatis ipsam sed doloremque ipsam dolores totam unde unde veritatis explicabo dicta quia dicta veritatis dicta sunt</p>
        <a class="more" href="#">Omnis ipsa sed <span class="arrow"><svg width="8" height="10" viewBox="0 0 8 10"><path d="M1 0l6 5-6 5z" fill="#fff"/></svg></span></a>
      </div>
    </div>
  </div>
</section>

<section class="section why">
  <div class="wrap">
    <h2 class="heading">Why choose us</h2>
    <div class="feature-grid">
      <div class="feature"><h3>Low price</h3><p>Fugit aut illo omnis explicabo ipsa ipsa, nemo rem ipsam quasi illo dolores ut voluptatem doloremque perspiciatis beatae magni architecto odit, aspernatur magni quae aperiam aut veritatis</p><a class="more" href="#">Veritatis unde <span class="arrow"><svg width="8" height="10" viewBox="0 0 8 10"><path d="M1 0l6 5-6 5z" fill="#fff"/></svg></span></a></div>
      <div class="feature"><h3>Free templates</h3><p>Fugit aut illo omnis explicabo ipsa ipsa, nemo rem ipsam quasi illo dolores ut voluptatem doloremque perspiciatis beatae magni architecto odit, aspernatur magni quae aperiam aut veritatis</p><a class="more" href="#">Veritatis unde <span class="arrow"><svg width="8" height="10" viewBox="0 0 8 10"><path d="M1 0l6 5-6 5z" fill="#fff"/></svg></span></a></div>
      <div class="feature"><h3>Designs by you</h3><p>Voluptas aut sit odit quasi quasi, unde quae ratione inventore ipsa explicabo iste sunt sed ipsam voluptatem consequuntur iste ipsam quasi quae ratione dolores consequuntur</p><a class="more" href="#">Sed enim <span class="arrow"><svg width="8" height="10" viewBox="0 0 8 10"><path d="M1 0l6 5-6 5z" fill="#fff"/></svg></span></a></div>
      <div class="divider"></div>
      <div class="feature"><h3>Special offer</h3><p>Fugit aut illo omnis explicabo ipsa ipsa, nemo rem ipsam quasi illo dolores ut voluptatem doloremque perspiciatis beatae magni architecto odit, aspernatur magni quae aperiam aut veritatis</p><a class="more" href="#">Veritatis unde <span class="arrow"><svg width="8" height="10" viewBox="0 0 8 10"><path d="M1 0l6 5-6 5z" fill="#fff"/></svg></span></a></div>
      <div class="feature"><h3>Hight quality</h3><p>Unde quasi quae ratione inventore ipsa ipsa explicabo iste sunt sed ipsam voluptatem consequuntur iste ipsam consequuntur quae ratione ratione dolores consequuntur consequuntur architecto sunt beatae</p><a class="more" href="#">Ratione inventore <span class="arrow"><svg width="8" height="10" viewBox="0 0 8 10"><path d="M1 0l6 5-6 5z" fill="#fff"/></svg></span></a></div>
      <div class="feature"><h3>Fast service</h3><p>Voluptas aut sit odit quasi quasi, unde quae ratione inventore ipsa explicabo iste sunt sed ipsam voluptatem consequuntur iste ipsam quasi quae ratione dolores consequuntur</p><a class="more" href="#">Sed enim <span class="arrow"><svg width="8" height="10" viewBox="0 0 8 10"><path d="M1 0l6 5-6 5z" fill="#fff"/></svg></span></a></div>
    </div>
  </div>
</section>

<section class="section gallery">
  <div class="wrap">
    <h2 class="heading">Templates gallery</h2>
    <div class="tabs">
      <span>Voluptas aut</span><span class="sep">|</span><span>sit odit quasi</span><span class="sep">|</span><span>unden quae ratione</span><span class="sep">|</span><span>inventore ipsa</span><span class="sep">|</span><span class="on">explicabo iste sunt</span><span class="sep">|</span><span>ipsam voluptatem</span>
      <span class="tab-arrows"><span class="arrow"><svg width="8" height="10" viewBox="0 0 8 10"><path d="M7 0L1 5l6 5z" fill="#fff"/></svg></span><span class="arrow"><svg width="8" height="10" viewBox="0 0 8 10"><path d="M1 0l6 5-6 5z" fill="#fff"/></svg></span></span>
    </div>
    <div class="tiles">
      <div class="tile-a" role="img" aria-label="Poster illustration of a crowned figure on a throne"></div>
      <div class="tile-b" role="img" aria-label="Poster illustration of a figure in red on a dark stage"></div>
      <div class="tile-c" role="img" aria-label="Poster illustration of a street with buildings at dusk"></div>
      <div class="tile-d"><h3>ILLO DOLORES</h3><p>nemo ipsam quasi illo dolores ut<br>voluptatem dolorem perspiciatis</p></div>
      <div class="tile-e" role="img" aria-label="Poster illustration of a rocket lifting off"></div>
      <div class="tile-f" role="img" aria-label="Poster illustration of a modern house with a person outside"></div>
    </div>
  </div>
</section>

<section class="section comments">
  <div class="wrap">
    <h2 class="heading">Customers comments</h2>
    <div class="comment-grid">
      <div class="comment"><div class="quote">“</div><p>Voluptas aut sit odit quasi quasi, unde quae ratione inventore ipsa explicabo iste sunt sed ipsam voluptatem consequuntur</p><div class="author"><span><b>Marco Velin</b> Student</span><span class="avatar" role="img" aria-label="Customer portrait"></span></div></div>
      <div class="comment"><div class="quote">“</div><p>Voluptas aut sit odit quasi quasi, unde quae ratione inventore ipsa explicabo iste sunt sed ipsam voluptatem consequuntur</p><div class="author"><span><b>Tobias</b> Lecture</span><span class="avatar" role="img" aria-label="Customer portrait"></span></div></div>
      <div class="comment"><div class="quote">“</div><p>Voluptas aut sit odit quasi quasi, unde quae ratione <b style="font-weight:400;color:var(--red)">inventore ipsa</b> explicabo iste sunt sed ipsam voluptatem consequuntur</p><div class="author"><span><b>Liora</b> Student</span><span class="avatar" role="img" aria-label="Customer portrait"></span></div></div>
    </div>
  </div>
</section>

<section class="section partners">
  <div class="wrap">
    <h2 class="heading">Best partner</h2>
    <div class="partner-row">
      <span class="badge" style="width:150px;height:34px"></span>
      <span class="badge" style="width:62px;height:62px"></span>
      <span class="badge" style="width:120px;height:40px"></span>
      <span class="badge" style="width:140px;height:34px"></span>
      <span class="badge" style="width:64px;height:64px"></span>
    </div>
  </div>
</section>

<section class="section tweet">
  <div class="wrap">
    <span class="tweet-dot"></span>
    <p>“I have never met a designer who was retained to keep things the same as they were.” Hafdís Lund prvk.is/q7Lm #PRENTA</p>
  </div>
</section>

<footer class="section footer">
  <div class="footer-cols">
    <div class="footer-col col-about">
      <h4>About Us</h4>
      <p>Fugit aut illo omnis explicabo ipsa, nemo ipsam quasi illo dolores ut voluptatem dolor perspiciatis beat ae magni architecto odit aut illo omnis explicabo ipsa ipsa nemo ipsam quasi</p>
      <a class="more" href="#">Read More <span class="arrow"><svg width="7" height="9" viewBox="0 0 8 10"><path d="M1 0l6 5-6 5z" fill="#fff"/></svg></span></a>
    </div>
    <div class="footer-col col-address">
      <h4>Address</h4>
      <ul class="address-list">
        <li><svg width="10" height="14" viewBox="0 0 10 14"><path d="M5 0a5 5 0 0 0-5 5c0 4 5 9 5 9s5-5 5-9a5 5 0 0 0-5-5z" fill="#fff"/><circle cx="5" cy="5" r="2" fill="#161616"/></svg>8 - 10 Tindagata Road Reykhólm RK4 2TT</li>
        <li><svg width="10" height="14" viewBox="0 0 10 14"><rect x="1" y="0" width="8" height="14" rx="1.5" fill="#fff"/><rect x="2.5" y="2" width="5" height="8" fill="#161616"/></svg>+02 318 640271<br>+02 318 640272</li>
        <li><svg width="12" height="9" viewBox="0 0 12 9"><rect width="12" height="9" fill="#fff"/><path d="M0 0l6 5 6-5" fill="none" stroke="#161616"/></svg>info@prentvik.is</li>
      </ul>
    </div>
    <div class="footer-col col-extra">
      <h4>Inventore ipsa</h4>
      <p>sed enim accusantium laudantium sunt perspiciatis ipsam sed doloremque ipsam dolores unde, et aut illo est veritatis explicabo dicta quia</p>
      <a class="more" href="#">Read More <span class="arrow"><svg width="7" height="9" viewBox="0 0 8 10"><path d="M1 0l6 5-6 5z" fill="#fff"/></svg></span></a>
    </div>
  </div>
  <div class="footer-bottom">
    <div class="wrap">
      <span>© 2013 YOURCOMPANY. All Rights Reserved</span>
      <span class="legal-links"><a href="#">about us</a>|<a href="#">customer service</a>|<a href="#">privacy policy</a>|<a href="#">contact us</a></span>
      <span class="socials"><span></span><span></span><span></span><span></span><span></span></span>
    </div>
  </div>
</footer>

</body>
</html>
```